Orva Business Card

we need a business card for flooring business called Orva Flooring, the design should be black and white. we have 2 locations

Ashmere Showroom
527 Kellerman Road,
Ashmere VIC 3128

Carrowdale Showroom
462 Bramwell Hwy,
Carrowdale VIC 3187

email : sales@orvaflooring.com.au
(03) 9471 2830

Please inform we sell , Laminate, Hybrid, Timber, carpet and commercial flooring

```html
<!DOCTYPE html>
<html lang="en">
<head>
<meta charset="utf-8">
<title>Orva Flooring Business Card</title>
<link rel="stylesheet" href="https://fonts.googleapis.com/css2?family=Arimo:wght@400;700&display=swap">
<style>
  :root {
    --stage: #d9d9d9;
    --stage-edge: #bdbdbd;
    --card: #333333;
    --ink: #ffffff;
    --ink-soft: #e6e6e6;
    --pill-ink: #2b2b2b;
  }
  * { box-sizing: border-box; margin: 0; padding: 0; }
  html, body { width: 1200px; height: 801px; overflow: hidden; }
  body {
    font-family: "Arimo", Arial, sans-serif;
    background: radial-gradient(ellipse at 35% 20%, var(--stage) 0%, var(--stage-edge) 100%);
    display: flex;
    align-items: center;
    justify-content: center;
    gap: 48px;
  }
  .card {
    width: 530px;
    height: 304px;
    background: var(--card);
    border-radius: 26px;
    color: var(--ink);
    position: relative;
    box-shadow: 0 10px 24px rgba(0,0,0,0.28);
  }

  /* Contact side */
  .card--contact { padding: 46px 36px; display: flex; }
  .contact-left {
    width: 232px;
    flex: none;
    display: flex;
    flex-direction: column;
    justify-content: space-between;
  }
  .brand { font-weight: 400; letter-spacing: 3px; line-height: 1.05; }
  .brand__name { font-size: 40px; display: block; }
  .brand__trade { font-size: 28px; display: block; }
  .person__name { font-weight: 700; font-size: 20px; letter-spacing: 0.5px; }
  .person__role { font-size: 15px; margin-top: 2px; color: var(--ink-soft); }
  .contact-line { display: flex; align-items: center; gap: 8px; font-size: 15px; margin-top: 6px; white-space: nowrap; }
  .contact-line svg { width: 14px; height: 14px; flex: none; }
  .divider { width: 1px; flex: none; background: var(--ink); margin: 0 22px; opacity: 0.85; }
  .showrooms { display: flex; flex-direction: column; justify-content: center; gap: 22px; }
  .showroom { font-size: 15px; line-height: 1.4; font-style: normal; white-space: nowrap; }

  /* Offer side */
  .card--offer {
    display: flex;
    flex-direction: column;
    align-items: center;
    justify-content: center;
    text-align: center;
  }
  .card--offer .brand__name { font-size: 64px; letter-spacing: 5px; }
  .card--offer .brand__trade { font-size: 40px; letter-spacing: 4px; }
  .we-sell {
    margin-top: 18px;
    background: var(--ink);
    color: var(--pill-ink);
    font-weight: 700;
    font-size: 18px;
    padding: 4px 16px;
    border-radius: 20px;
  }
  .products {
    list-style: none;
    display: flex;
    gap: 10px;
    margin-top: 14px;
    font-size: 15.5px;
    white-space: nowrap;
  }
  .products li::before { content: "● "; font-size: 11px; vertical-align: 2px; }
</style>
</head>
<body>

  <article class="card card--contact">
    <div class="contact-left">
      <div class="brand">
        <span class="brand__name">ORVA</span>
        <span class="brand__trade">FLOORING</span>
      </div>
      <div class="person">
        <p class="person__name">MARCUS HALE</p>
        <p class="person__role">Manager</p>
        <p class="contact-line">
          <svg viewBox="0 0 16 16" aria-hidden="true"><path d="M3 1.5l3 3-1.6 1.8c.9 2 2.4 3.5 4.3 4.3L10.5 9l3 3-1.8 2.3C6.8 14 2 9.2 1.7 4.3z" fill="none" stroke="#fff" stroke-width="1.4" stroke-linejoin="round"/></svg>
          (03) 9471 2830
        </p>
        <p class="contact-line">
          <svg viewBox="0 0 16 16" aria-hidden="true"><rect x="1.5" y="3.5" width="13" height="9" rx="1" fill="none" stroke="#fff" stroke-width="1.4"/><path d="M1.5 4l6.5 5 6.5-5" fill="none" stroke="#fff" stroke-width="1.4"/></svg>
          sales@orvaflooring.com.au
        </p>
      </div>
    </div>
    <div class="divider"></div>
    <div class="showrooms">
      <address class="showroom">Carrowdale Showroom<br>462 Bramwell Hwy,<br>Carrowdale VIC 3187</address>
      <address class="showroom">Ashmere Showroom<br>527 Kellerman Road,<br>Ashmere VIC 3128</address>
    </div>
  </article>

  <article class="card card--offer">
    <div class="brand">
      <span class="brand__name">ORVA</span>
      <span class="brand__trade">FLOORING</span>
    </div>
    <p class="we-sell">We Sell</p>
    <ul class="products">
      <li>Laminate</li>
      <li>Hybrid</li>
      <li>Timber</li>
      <li>carpet</li>
      <li>commercial flooring</li>
    </ul>
  </article>

</body>
</html>
```